Business Landing Page for SEO Company

Need the landing page of the website designed - I will provide the copy, will need to include details of my company and the services offered, about us, testimonials, faq, etc., and all these elements will need to be arranged graphically on the page.

I want something similar to this: https://pebrovault.com/

Not in terms of color or theme or anything, but we offer a similar service and want to display similar information.

Th services we provide are:

Premium Links
Monthly Links Subscription
Link Insertions

Need to advertise them on the front page. Additionally need a place for testimonials, company details, etc.,

We already have logo for the website. Please use the attached file to insert the logo within the overal design.

Target Market(s)

SEO marketers and agencies

Number of Pages Required

1 page

```html
<!DOCTYPE html>
<html lang="en">
<head>
<meta charset="utf-8">
<title>Linkora – SEO Services</title>
<link href="https://fonts.googleapis.com/css2?family=Montserrat:wght@400;500;600;700&display=swap" rel="stylesheet">
<style>
:root{
  --blue:#2b86e3;
  --orange:#f2622e;
  --ink:#2c2c2c;
  --muted:#8a8a8a;
  --line:#e6e9ee;
  --band:#deedfc;
  --soft:#f6f6f6;
  --footer:#f3f3f3;
  --bar:#3a3a3a;
}
*{box-sizing:border-box;margin:0;padding:0}
html,body{width:1200px;height:4485px;overflow:hidden}
body{font-family:"Montserrat",sans-serif;color:var(--ink);background:#fff;position:relative}
section,header,footer{position:absolute;left:0;width:1200px}
.abs{position:absolute}
.center{text-align:center;left:0;width:1200px}
.h2{font-size:21px;font-weight:500;color:var(--ink)}
.sub{font-size:11px;color:var(--muted);line-height:19px}
.btn{position:absolute;background:var(--blue);color:#fff;font-size:11px;font-weight:600;display:flex;align-items:center;justify-content:center;border-radius:2px}
.art{position:absolute;border-radius:10px}

/* header */
.site-header{top:0;height:61px;border-bottom:2px solid var(--line)}
.logo{left:162px;top:13px;font-size:27px;font-weight:600;color:var(--blue)}
.nav{left:393px;top:23px;display:flex;gap:25px;font-size:11px;color:var(--muted)}
.nav .active{color:var(--blue)}
.head-cta{left:911px;top:15px;width:128px;height:31px;background:var(--orange);font-weight:500}

/* hero */
.hero{top:61px;height:447px;border-bottom:1px solid var(--line)}
.hero h1{left:159px;top:118px;font-size:31px;font-weight:500;line-height:37px;letter-spacing:.5px}
.hero p{left:161px;top:249px;font-size:10px;color:var(--muted)}
.hero .field{left:161px;top:286px;width:226px;height:34px;border:1px solid var(--line);font-size:10px;color:var(--muted);padding:11px 16px}
.hero .btn{left:401px;top:286px;width:128px;height:34px}

/* services */
.services{top:508px;height:467px}
.card{position:absolute;top:152px;width:278px;height:224px;border:1px solid var(--line);text-align:center}
.card.active{border-color:var(--blue)}
.card svg{margin-top:26px}
.card h3{font-size:14px;font-weight:500;margin-top:16px}
.card.active h3,.card.active .more{color:var(--blue)}
.card p{font-size:10px;color:var(--muted);line-height:19px;margin:14px 22px 0}
.card .more{font-size:10px;font-weight:600;margin-top:14px}

/* seo band */
.band{top:975px;height:428px;background:var(--band)}
.band h2{left:161px;top:116px;font-size:19px;font-weight:500;line-height:30px}
.band p{left:161px;top:189px;width:380px;font-size:10px;color:var(--muted);line-height:19px}
.band .btn{left:162px;top:276px;width:127px;height:33px}

/* testimonials */
.testi{top:1403px;height:498px}
.quote{top:171px;font-size:17px;line-height:27px}
.avatar{left:578px;top:269px;width:44px;height:44px;border-radius:50%;background:linear-gradient(#7b6a5e,#3d3633)}
.dots{left:571px;top:407px;display:flex;gap:8px}
.dots span{width:14px;height:2px;background:var(--line)}
.dots .on{background:var(--blue)}

/* faq */
.faq{top:1901px;height:794px;background:var(--soft)}
.qa{position:absolute;left:263px;width:674px;border:1px solid #cfd6df;background:#fff;font-size:14px;font-weight:500;letter-spacing:1px;text-align:center}
.qa .q{height:42px;display:flex;align-items:center;justify-content:center;position:relative}
.qa .q b{position:absolute;right:22px;color:var(--blue);font-weight:500;font-size:16px}
.qa.open{border-color:var(--blue)}
.qa.open .q{background:var(--blue);color:#fff}
.qa.open .q b{color:#fff}
.qa .a{font-size:13px;letter-spacing:.5px;line-height:23px;padding:16px 88px 18px}

/* pricing */
.pricing{top:2695px;height:688px}
.plan{position:absolute;top:186px;width:278px;height:409px;border:1px solid var(--line);text-align:center}
.plan.active{border-color:var(--blue)}
.plan h4{font-size:14px;font-weight:500;margin-top:22px}
.plan .price{font-size:37px;color:var(--blue);font-weight:500;margin-top:8px}
.plan .per{font-size:10px;color:var(--muted);margin-top:6px}
.plan hr{border:0;border-top:1px solid var(--line);width:200px;margin:28px auto 32px}
.plan.active hr{border-color:var(--blue)}
.plan li{list-style:none;font-size:11.5px;color:var(--muted);line-height:30px}
.plan .btn{left:78px;top:351px;width:120px;height:33px}

/* cta */
.cta{top:3383px;height:134px;background:var(--band)}
.cta h2{left:159px;top:56px;font-size:20px;font-weight:500}
.cta .btn{left:888px;top:48px;width:151px;height:37px}

/* contact */
.contact{top:3517px;height:597px}
.in{position:absolute;height:43px;border:1px solid #cdd3da;font-size:10px;font-style:italic;font-weight:600;padding:15px 27px}
.in.focus{border-color:var(--blue)}
.contact .btn{left:218px;top:461px;width:764px;height:44px;border-radius:3px}

/* footer */
.site-footer{top:4114px;height:334px;background:var(--footer)}
.col{position:absolute;top:79px}
.col h5{font-size:15px;font-weight:500;margin-bottom:14px}
.col a{display:block;font-size:10.5px;color:var(--muted);line-height:23px;text-decoration:none}
.nl{left:812px;top:130px;width:150px;height:34px;background:#fff;font-size:10px;color:var(--muted);padding:12px 14px}
.site-footer .btn{left:963px;top:130px;width:76px;height:34px}
.social{left:813px;top:229px;display:grid;grid-template-columns:88px 82px 80px;row-gap:8px;font-size:10.5px;color:var(--muted)}
.social span{display:flex;align-items:center;gap:5px}
.social i{width:6px;height:6px;border-radius:50%;background:var(--blue);display:block}
.bottom{top:4448px;height:37px;background:var(--bar);color:#fff;font-size:10px;display:flex;align-items:center;justify-content:center}
</style>
</head>
<body>

<header class="site-header">
  <div class="abs logo">Linkora</div>
  <nav class="abs nav"><span>Home</span><span class="active">Services</span><span>About Us</span><span>Testimonials</span><span>FAQ</span><span>Contact Us</span></nav>
  <div class="btn head-cta">Free SEO Analysis</div>
</header>

<section class="hero">
  <h1 class="abs">Let us Grow and Optimise<br>Your Website Traffic for<br>Better Results.</h1>
  <p class="abs">SEO is mandatory for your website to stand out. So try now</p>
  <div class="abs field">Your website link</div>
  <div class="btn">Get Free Analysis</div>
  <div class="art" role="img" aria-label="Illustration of two people examining a website with a large magnifying glass" style="left:636px;top:52px;width:383px;height:287px;background:linear-gradient(160deg,#f1f4f8,#dde9f7 55%,#f6f7f9)"></div>
</section>

<section class="services">
  <div class="abs center h2" style="top:34px">Our Services</div>
  <div class="abs center sub" style="top:72px">Check out our services and choose what suit your need for better<br>results for your website</div>
  <div class="card" style="left:162px">
    <svg width="28" height="28" viewBox="0 0 24 24" fill="none" stroke="#2c2c2c" stroke-width="1.5"><path d="M10 14a4 4 0 0 0 5.7 0l3-3a4 4 0 0 0-5.7-5.7l-1 1"/><path d="M14 10a4 4 0 0 0-5.7 0l-3 3a4 4 0 0 0 5.7 5.7l1-1"/></svg>
    <h3>Premium Links</h3>
    <p>Ut enim ad minima veniam, quis nostrum exercitationem ullam corporis suscipit laboriosam, nisi ut aliquid.</p>
    <div class="more">Read More →</div>
  </div>
  <div class="card active" style="left:461px">
    <svg width="28" height="28" viewBox="0 0 24 24" fill="none" stroke="#2b86e3" stroke-width="1.5"><path d="M10 14a4 4 0 0 0 5.7 0l3-3a4 4 0 0 0-5.7-5.7l-1 1"/><path d="M14 10a4 4 0 0 0-5.7 0l-3 3a4 4 0 0 0 5.7 5.7l1-1"/></svg>
    <h3>Monthly Links Subscription</h3>
    <p>Lorem ipsum dolor sit amet, consectetur adipiscing elit, sed do eiusmod tempor incididunt ut labore et dolore.</p>
    <div class="more">Read More →</div>
  </div>
  <div class="card" style="left:761px">
    <svg width="28" height="28" viewBox="0 0 24 24" fill="none" stroke="#2c2c2c" stroke-width="1.5"><path d="M10 14a4 4 0 0 0 5.7 0l3-3a4 4 0 0 0-5.7-5.7l-1 1"/><path d="M14 10a4 4 0 0 0-5.7 0l-3 3a4 4 0 0 0 5.7 5.7l1-1"/></svg>
    <h3>Link Insertions</h3>
    <p>Sed ut perspiciatis unde omnis iste natus error sit voluptatem accusantium doloremque laudantium.</p>
    <div class="more">Read More →</div>
  </div>
</section>

<section class="band">
  <h2 class="abs">SEO is the key to get ahead in nowdays<br>and rank higher</h2>
  <p class="abs">Lorem ipsum dolor sit amet, consectetur adipiscing elit, sed do eiusmod tempor incididunt ut labore et dolore magna aliqua. Ut enim ad minim veniam quis nostrud.</p>
  <div class="btn">Learn More</div>
  <div class="art" role="img" aria-label="Illustration of a person searching a large browser window with a magnifying glass" style="left:679px;top:78px;width:296px;height:279px;background:linear-gradient(160deg,#eef3f9,#c9def6 55%,#e6eef8)"></div>
</section>

<section class="testi">
  <div class="abs center h2" style="top:90px">Testimonials</div>
  <div class="abs center sub" style="top:127px">See what our lovely customers saying about working with us.</div>
  <div class="abs center quote">No doubt this people service was very efficient, we've<br>been looking for a service like this, we got more than<br>what we asked for, Thanks SEO Service.</div>
  <div class="abs avatar" role="img" aria-label="Customer portrait"></div>
  <div class="abs center" style="top:333px;font-size:13px;font-weight:500">Ethan Mercer</div>
  <div class="abs center" style="top:362px;font-size:8.5px;color:var(--blue)">CEO &amp; Co Founder of Voltline Motors</div>
  <div class="abs dots"><span></span><span class="on"></span><span></span></div>
</section>

<section class="faq">
  <div class="abs center h2" style="top:87px">Frequently Asked Questions</div>
  <div class="abs center sub" style="top:126px">Find the answers to your questions</div>
  <div class="qa" style="top:186px"><div class="q">How to work with us?<b>+</b></div></div>
  <div class="qa open" style="top:254px"><div class="q">How long it takes to see results?<b>–</b></div>
    <div class="a">Lorem ipsum dolor sit amet, consectetur adipiscing elit, sed do eiusmod tempor incididunt ut labore et dolore magna aliqua. enim ad minim veniam, quis nostrud exercitation ullamco laboris nisi ut aliquip ex ea commodo consequat.</div></div>
  <div class="qa" style="top:446px"><div class="q">How does it works?<b>+</b></div></div>
  <div class="qa" style="top:514px"><div class="q">How to get a monthly subscription?<b>+</b></div></div>
  <div class="qa" style="top:580px"><div class="q">How to get premium links?<b>+</b></div></div>
  <div class="btn" style="left:536px;top:670px;width:128px;height:34px">More Questions</div>
</section>

<section class="pricing">
  <div class="abs center h2" style="top:87px">Our Pricing</div>
  <div class="abs center sub" style="top:126px">Check out our pricing plan</div>
  <div class="plan" style="left:162px"><h4>Basic</h4><div class="price">$29.99</div><div class="per">per month</div><hr>
    <ul><li>Limited SEO &amp; Ranking</li><li>3 Analytics Campaigns</li><li>200 Keywords</li><li>Ranking up to fifth page</li><li>3 updates</li></ul><div class="btn">Purchase Plan</div></div>
  <div class="plan active" style="left:461px"><h4>Pro</h4><div class="price">$84.99</div><div class="per">per month</div><hr>
    <ul><li>Limited SEO &amp; Ranking</li><li>9 Analytics Campaigns</li><li>600 Keywords</li><li>Ranking up to third page</li><li>Unlimited updates</li></ul><div class="btn">Purchase Plan</div></div>
  <div class="plan" style="left:761px"><h4>Advanced</h4><div class="price">$199.99</div><div class="per">per month</div><hr>
    <ul><li>Limited SEO &amp; Ranking</li><li>45 Analytics Campaigns</li><li>1800 Keywords</li><li>Ranking up to first page</li><li>Unlimited updates</li></ul><div class="btn">Purchase Plan</div></div>
</section>

<section class="cta">
  <h2 class="abs">Ready to improve and take your SEO to the next level?</h2>
  <div class="btn">Get Free Seo Analysis</div>
</section>

<section class="contact">
  <div class="abs center h2" style="top:87px">Contact Us</div>
  <div class="abs center sub" style="top:126px">Feel free to contact us for any inquiry</div>
  <div class="in focus" style="left:218px;top:183px;width:372px">Your Name</div>
  <div class="in" style="left:608px;top:183px;width:374px">Your Email</div>
  <div class="in" style="left:218px;top:243px;width:372px">Your Phone</div>
  <div class="in" style="left:608px;top:243px;width:374px">Project Type</div>
  <div class="in" style="left:218px;top:305px;width:764px;height:133px">Your Message</div>
  <div class="btn">Submit Message&nbsp;
    <svg width="10" height="10" viewBox="0 0 24 24" fill="#fff"><path d="M2 21 23 12 2 3v7l15 2-15 2z"/></svg></div>
</section>

<footer class="site-footer">
  <div class="col" style="left:162px"><h5>Menu</h5><a>Home</a><a>Services</a><a>About Us</a><a>Testimonials</a><a>Contact Us</a></div>
  <div class="col" style="left:386px"><h5>Services</h5><a>Premium Links</a><a>Monthly Links Subscription</a><a>Link Insertions</a></div>
  <div class="col" style="left:612px"><h5>Our Policy</h5><a>Terms &amp; Conditions</a><a>Privacy Policy</a><a>FAQ</a></div>
  <div class="col" style="left:812px"><h5>Newsletter</h5></div>
  <div class="abs nl">Email Address</div>
  <div class="btn">Sign Up</div>
  <div class="abs" style="left:813px;top:195px;font-size:15px;font-weight:500">Social</div>
  <div class="abs social"><span><i></i>Friendnest</span><span><i></i>Chirply</span><span><i></i>Pinboardly</span><span><i></i>Workline</span><span><i></i>Snapgram</span></div>
</footer>
<div class="abs bottom" style="left:0;width:1200px">Copyright © Business Name 2021 All Rights Reserved.</div>

</body>
</html>
```